Not-for-profit industry infographic

We are looking to take content from our proposals and turn it into an infographic. There is a lot of text, but we are okay with it being trimmed back so that people will actually read it! Our goal is to try to graphically display as much of this content as possible. Icons and other images are encouraged. Once a designer is chosen, we would like to continue to work with them for future infographics of the same style. Attached are our colors.

Target Market(s)

CFOs, COOs, controllers in the Not-for-profit industry.

Industry/Entity Type

Industry

Font styles to use
Sans Serif

Requirements
Must have
• The infographic will have to be placed back into the proposals, so it will need to be on a white background.

```html
<!DOCTYPE html>
<html lang="en">
<head>
<meta charset="utf-8">
<title>Not-for-profit services infographic</title>
<link href="https://fonts.googleapis.com/css2?family=Source+Sans+3:wght@400;600&display=swap" rel="stylesheet">
<style>
  :root {
    --white: #ffffff;
    --cyan: #00f7ff;
    --navy: #1d2a6b;
    --red: #ef3a24;
    --orange: #f7901e;
    --yellow: #ffd600;
    --frame-yellow: #ffe600;
    --frame-red: #ff2346;
    --tab-grey: #f4f5f8;
  }
  * { box-sizing: border-box; margin: 0; padding: 0; }
  html, body { width: 1145px; height: 1200px; overflow: hidden; background: var(--white); }
  body { font-family: "Source Sans 3", "Myriad Pro", Arial, sans-serif; position: relative; }

  .section-label {
    position: absolute;
    background: var(--cyan);
    border: 5px solid;
    border-image: linear-gradient(90deg, var(--frame-yellow), var(--frame-red)) 1;
    color: var(--white);
    font-size: 27px;
    display: flex;
    align-items: center;
    justify-content: center;
  }
  .label-training { left: 186px; top: 3px; width: 391px; height: 66px; }
  .label-industry { left: 198px; top: 740px; width: 372px; height: 70px; }

  .benefit-tab {
    position: absolute;
    background: var(--tab-grey);
    box-shadow: -6px 0 14px rgba(0,0,0,0.06);
  }
  .benefit-tab svg { position: absolute; left: 18px; top: 50%; transform: translateY(-50%); }
  .tab-newsletter { left: 226px; top: 157px; width: 100px; height: 236px; }
  .tab-webinars  { left: 223px; top: 435px; width: 100px; height: 233px; }

  .orange-pill {
    position: absolute;
    background: linear-gradient(90deg, var(--red) 0%, var(--orange) 50%, var(--yellow) 100%);
    color: var(--white);
    font-size: 20px;
    line-height: 28px;
    display: flex;
    align-items: center;
    box-shadow: 0 0 0 4px rgba(255,230,0,0.55), 0 6px 14px rgba(239,58,36,0.18);
  }
  .pill-newsletter { left: 320px; top: 192px; width: 654px; height: 168px; border-radius: 0 84px 84px 0; padding: 0 40px 0 28px; }
  .pill-webinars  { left: 317px; top: 465px; width: 653px; height: 168px; border-radius: 0 84px 84px 0; padding: 0 40px 0 32px; }
  .pill-involvement { left: 201px; top: 875px; width: 788px; height: 171px; border-radius: 86px; padding: 0 40px 0 56px; }

  .association-list {
    position: absolute;
    left: 204px; top: 1080px; width: 565px; height: 118px;
    background: var(--cyan);
    border: 5px solid;
    border-image: linear-gradient(90deg, var(--frame-yellow), var(--frame-red)) 1;
    color: var(--navy);
    font-size: 20px;
    line-height: 28px;
    padding: 20px 0 0 20px;
    list-style: none;
  }
</style>
</head>
<body>
  <div class="section-label label-training">Access to customized training</div>

  <div class="benefit-tab tab-newsletter">
    <svg width="66" height="66" viewBox="0 0 66 66" aria-hidden="true">
      <defs><linearGradient id="gem1" x1="0" y1="0" x2="1" y2="1"><stop offset="0" stop-color="#ffe27a"/><stop offset="1" stop-color="#f7a21e"/></linearGradient></defs>
      <rect x="14" y="14" width="38" height="38" rx="8" transform="rotate(45 33 33)" fill="url(#gem1)" stroke="#f26a21" stroke-width="4"/>
    </svg>
  </div>
  <div class="orange-pill pill-newsletter">
    <p>You’ll receive “LedgerBrief,” a monthly email newsletter that covers technical changes impacting the not-for-profit industry and features specially curated news and insight.</p>
  </div>

  <div class="benefit-tab tab-webinars">
    <svg width="66" height="66" viewBox="0 0 66 66" aria-hidden="true">
      <defs><linearGradient id="gem2" x1="0" y1="0" x2="1" y2="1"><stop offset="0" stop-color="#ffe27a"/><stop offset="1" stop-color="#f7a21e"/></linearGradient></defs>
      <rect x="14" y="14" width="38" height="38" rx="8" transform="rotate(45 33 33)" fill="url(#gem2)" stroke="#f26a21" stroke-width="4"/>
    </svg>
  </div>
  <div class="orange-pill pill-webinars">
    <p>Additionally, you will receive invitations to quarterly webinars specific to the public sector, hosted by Halvorsen’s dedicated team of professionals.</p>
  </div>

  <div class="section-label label-industry">Industry involvement</div>

  <div class="orange-pill pill-involvement">
    <p>Halvorsen is actively involved in industry associations that provide access to professionals with not-for-profit experience across the country. Our executives participate in various industry groups as both speakers and attendees, including:</p>
  </div>

  <ul class="association-list">
    <li>Lakeshore Nonprofit Alliance</li>
    <li>Council of Great Lakes Foundations</li>
    <li>State and national CPA nonprofit conferences</li>
  </ul>
</body>
</html>
```